TBranwell executive consulting

We need a basic clean website for executive consulting. Rosalind is the previos CIO for bluecrest airways and currently supports several technology companies with innovation and transformation.

Target Market(s)

C level technology and CIO training

Industry/Entity Type

Technology and travel industry

Coding

Coded - Design and coding required

Number of Pages Required

3 page

Font styles to use
Sans Serif

Colors
0054AA
0677BA
7BADD7
CADEEF
E8F1F8
0094D4
00A9DD
6FCCEA
C7EBF8
E9F6FB

Requirements
Must have
• Home page, about us, services social media links

```html
<!DOCTYPE html>
<html lang="en">
<head>
<meta charset="utf-8">
<title>TBranwell Executive Consulting</title>
<link href="https://fonts.googleapis.com/css2?family=Orbitron:wght@600;700&family=Jost:ital,wght@0,400;0,500;0,600;1,400&display=swap" rel="stylesheet">
<style>
:root{
  --navy:#0054AA;--blue:#0677BA;--sky:#7BADD7;--mist:#CADEEF;--ice:#E8F1F8;
  --cyan:#0094D4;--aqua:#00A9DD;--light-aqua:#6FCCEA;--pale:#C7EBF8;--frost:#E9F6FB;
  --ink:#1d1d22;--text:#555a60;--footer:#232327;--grey-bg:#e9e9ea;
  --btn:linear-gradient(90deg,#0a8fc4,#0677BA);
}
*{box-sizing:border-box;margin:0;padding:0}
html,body{width:1200px;height:3129px;overflow:hidden}
body{font-family:"Jost",sans-serif;color:var(--ink);background:#fff;position:relative}
.heading{font-family:"Orbitron",sans-serif;font-weight:700}
.btn{position:absolute;display:flex;align-items:center;justify-content:space-between;border-radius:30px;background:var(--btn);color:#fff;font-weight:600;font-size:13.5px;padding:0 5px 0 22px;text-transform:uppercase;text-decoration:none}
.btn .arrow{width:38px;height:38px;border-radius:50%;background:#fff;display:flex;align-items:center;justify-content:center}

/* header */
.site-header{position:absolute;top:0;left:0;width:1200px;height:88px;background:#fff;border-bottom:1px solid #ddd}
.brand{position:absolute;left:109px;top:20px;display:flex;align-items:center;gap:10px;font-family:"Orbitron",sans-serif;font-weight:700;font-size:34px;color:var(--blue)}
.brand .dot{width:14px;height:14px;border-radius:50%;background:var(--aqua)}
.main-nav{position:absolute;left:423px;top:22px;width:481px;height:46px;border-radius:24px;background:#ececec;display:flex;align-items:center;font-size:12.5px;text-transform:uppercase;color:#333}
.main-nav a{padding:0 24px;height:46px;display:flex;align-items:center;text-decoration:none;color:inherit}
.main-nav a.active{background:var(--btn);color:#fff;border-radius:24px;padding:0 28px}

/* hero */
.hero{position:absolute;top:88px;left:0;width:1200px;height:738px;background:radial-gradient(ellipse at 50% 30%,#0a6fb0 0%,#0a4a86 40%,#08264d 75%,#061a35 100%);overflow:hidden}
.hero-kicker{position:absolute;top:196px;width:100%;text-align:center;color:#fff;font-size:36px;letter-spacing:1px}
.hero-title{position:absolute;top:232px;width:100%;text-align:center;color:#fff;font-size:118px;line-height:1;letter-spacing:2px}
.hero-sub{position:absolute;top:368px;left:240px;width:720px;text-align:center;color:#fff;font-size:13px;font-weight:500;line-height:22px}
.scroll-cue{position:absolute;left:568px;top:586px;width:64px;height:113px;border:2px solid #fff;border-radius:32px;display:flex;align-items:center;justify-content:center}

/* about */
.about{position:absolute;top:826px;left:0;width:1200px;height:600px;background:linear-gradient(#fff 60%,#ececed)}
.photo{position:absolute;border-radius:10px}
.about-title{position:absolute;left:635px;top:112px;font-size:37px;line-height:46px;color:var(--ink)}
.about-copy{position:absolute;left:635px;top:212px;width:425px;font-size:12.3px;line-height:22px;color:var(--text)}
.about-copy p+p{margin-top:14px}

/* services */
.services{position:absolute;top:1426px;left:0;width:1200px;height:800px;background:var(--grey-bg)}
.section-title{position:absolute;width:100%;text-align:center;font-size:37px}
.service{position:absolute;width:290px;text-align:center}
.service .num{font-family:"Orbitron",sans-serif;font-size:28px;color:#c4c4c6;font-weight:600;line-height:30px}
.service .icon{width:102px;height:102px;border-radius:50%;margin:12px auto 0;background:linear-gradient(135deg,#1aa5d6,#0677BA 60%,#0a5a95)}
.service h3{font-size:17.5px;line-height:22px;margin-top:20px;font-weight:700}
.service p{font-size:12.3px;line-height:22px;color:var(--text);margin:12px auto 0;width:255px}

/* testimonials */
.testimonials{position:absolute;top:2226px;left:0;width:1200px;height:509px;background:#fff}
.quote-mark{position:absolute;left:560px;top:60px;font-family:Georgia,serif;font-size:150px;line-height:1;color:#e2e2e4}
.avatar{position:absolute;left:531px;top:144px;width:138px;height:138px;border-radius:50%;border:4px solid var(--cyan);padding:5px}
.avatar span{display:block;width:100%;height:100%;border-radius:50%;background:linear-gradient(#d8dde2,#8a96a3)}
.quote{position:absolute;left:210px;top:308px;width:780px;text-align:center;font-style:italic;font-size:14.5px;line-height:22px;color:#666}
.client{position:absolute;top:392px;width:100%;text-align:center;font-size:17px}
.client-role{position:absolute;top:418px;width:100%;text-align:center;font-size:12px;color:#666}
.nav-arrow{position:absolute;top:300px;width:41px;height:41px;border-radius:50%;display:flex;align-items:center;justify-content:center}

/* footer */
.site-footer{position:absolute;top:2735px;left:0;width:1200px;height:394px;background:var(--footer);color:#fff}
.foot-brand{position:absolute;left:113px;top:142px;display:flex;align-items:center;gap:10px;font-family:"Orbitron",sans-serif;font-weight:700;font-size:40px;color:#fff}
.foot-brand .dot{width:16px;height:16px;border-radius:50%;background:var(--aqua)}
.foot-col h4{font-size:19px;margin-bottom:22px}
.foot-col{position:absolute;top:73px}
.foot-links a{display:block;color:#ddd;font-size:13px;text-decoration:none;line-height:31px}
.contact-item{display:flex;gap:12px;margin-bottom:16px}
.contact-item b{display:block;font-weight:500;font-size:13.5px}
.contact-item span{font-size:12.8px;color:#ddd;line-height:17px;display:block}
.socials{display:flex;gap:9px}
.socials span{width:41px;height:41px;border-radius:50%;background:#38383d}
.socials span:first-child{background:var(--btn)}
.foot-rule{position:absolute;left:122px;top:338px;width:956px;height:1px;background:#3c3c41}
.copyright{position:absolute;top:358px;width:100%;text-align:center;font-size:13px}
.to-top{position:absolute;left:1127px;top:311px;width:51px;height:51px;border-radius:50%;background:var(--btn);display:flex;align-items:center;justify-content:center}
</style>
</head>
<body>

<header class="site-header">
  <div class="brand"><span class="dot"></span>TB</div>
  <nav class="main-nav">
    <a class="active" href="#">Home</a><a href="#">About Us</a><a href="#">Services</a><a href="#">Social Media Links</a>
  </nav>
  <a class="btn" style="left:940px;top:22px;width:170px;height:46px">Contact Us
    <span class="arrow"><svg width="18" height="14" viewBox="0 0 18 14"><path d="M1 7h15M10 1l6 6-6 6" fill="none" stroke="#0677BA" stroke-width="1.8"/></svg></span></a>
</header>

<section class="hero" role="img" aria-label="Night city skyline with glowing network lights">
  <div class="hero-kicker heading">Innovating the Future of</div>
  <h1 class="hero-title heading">Technology</h1>
  <p class="hero-sub">Rosalind Branwell, former Chief Information Officer of Bluecrest Airways, now supports several technology companies with innovation and transformation.</p>
  <a class="btn" style="left:499px;top:434px;width:198px;height:44px">Explore Services
    <span class="arrow" style="width:36px;height:36px"><svg width="18" height="14" viewBox="0 0 18 14"><path d="M1 7h15M10 1l6 6-6 6" fill="none" stroke="#0677BA" stroke-width="1.8"/></svg></span></a>
  <div class="scroll-cue"><svg width="26" height="40" viewBox="0 0 26 40"><path d="M13 2v34M3 26l10 11 10-11" fill="none" stroke="#fff" stroke-width="2"/></svg></div>
</section>

<section class="about">
  <div class="photo" role="img" aria-label="Executive holding a tablet with digital graphics" style="left:259px;top:91px;width:215px;height:214px;background:linear-gradient(135deg,#3b4f66,#1d3552 55%,#4fa6d3)"></div>
  <div class="photo" role="img" aria-label="Digital figure wearing a VR headset" style="left:142px;top:244px;width:215px;height:215px;background:linear-gradient(135deg,#0a4f86,#0e86c4 55%,#0a3a6a)"></div>
  <div class="photo" role="img" aria-label="Portrait of Rosalind Branwell" style="left:366px;top:312px;width:215px;height:213px;background:linear-gradient(135deg,#c9c0b3,#5c4a40 60%,#2a2a2e)"></div>
  <h2 class="about-title heading">About Us<br>Rosalind Branwell</h2>
  <div class="about-copy">
    <p>Rosalind Branwell is a seasoned leader with a remarkable 40-year career in the travel industry, including 20 transformative years at Bluecrest Airways. As the Senior Vice President of Technology (CIO), Rosalind spearheaded some of the company's most significant technological and strategic transformations, helping Bluecrest Airways stay at the forefront of innovation in the competitive travel market. Her work bridged the gap between business strategy and technology, driving measurable success and resilience.</p>
    <p>With expertise in Leadership, Mentorship, Technology Strategy, and Digital Transformation, Rosalind is passionate about empowering IT leaders to forge stronger connections between their technology teams and business goals. Her approach is rooted in a belief that technology is not just a tool but a catalyst for growth, collaboration, and innovation.</p>
  </div>
</section>

<section class="services">
  <h2 class="section-title heading" style="top:24px">Our Services</h2>
  <div class="service" style="left:136px;top:90px"><div class="num">01</div><div class="icon" role="img" aria-label="Strategy icon"></div><h3 class="heading">Technology Strategy<br>Development</h3><p>Aligning IT strategies with business goals for growth and innovation.</p></div>
  <div class="service" style="left:455px;top:90px"><div class="num">02</div><div class="icon" role="img" aria-label="Transformation icon"></div><h3 class="heading">Digital Transformation<br>Consulting</h3><p>Implementing modern technology solutions to improve efficiency...</p></div>
  <div class="service" style="left:774px;top:90px"><div class="num">03</div><div class="icon" role="img" aria-label="Partnership icon"></div><h3 class="heading">IT-Business Partnership<br>Development</h3><p>Strengthening collaboration between IT and business units for seamless decision...</p></div>
  <div class="service" style="left:136px;top:398px"><div class="num">04</div><div class="icon" role="img" aria-label="Change management icon"></div><h3 class="heading">Organizational Change<br>Management</h3><p>Guiding companies through large-scale IT and organizational changes.</p></div>
  <div class="service" style="left:455px;top:398px"><div class="num">05</div><div class="icon" role="img" aria-label="Project oversight icon"></div><h3 class="heading">Program and Project<br>Oversight</h3><p>Ensuring technology initiatives meet business objectives and timelines.</p></div>
  <div class="service" style="left:774px;top:398px"><div class="num">06</div><div class="icon" role="img" aria-label="Advisory icon"></div><h3 class="heading">Advisory Services for<br>CIOs &amp; IT Executives</h3><p>Strategic guidance for senior IT leaders on leadership, communication...</p></div>
  <a class="btn" style="left:499px;top:701px;width:203px;height:46px">View All Services
    <span class="arrow" style="width:38px;height:38px"><svg width="18" height="14" viewBox="0 0 18 14"><path d="M1 7h15M10 1l6 6-6 6" fill="none" stroke="#0677BA" stroke-width="1.8"/></svg></span></a>
</section>

<section class="testimonials">
  <div class="quote-mark">&ldquo;</div>
  <h2 class="section-title heading" style="top:82px">Testimonials</h2>
  <div class="avatar"><span role="img" aria-label="Portrait of Marcus Hale"></span></div>
  <div class="nav-arrow" style="left:46px;background:#1d1d22"><svg width="16" height="12" viewBox="0 0 16 12"><path d="M15 6H2M7 1 2 6l5 5" fill="none" stroke="#fff" stroke-width="1.6"/></svg></div>
  <div class="nav-arrow" style="left:1070px;background:var(--btn)"><svg width="16" height="12" viewBox="0 0 16 12"><path d="M1 6h13M9 1l5 5-5 5" fill="none" stroke="#fff" stroke-width="1.6"/></svg></div>
  <p class="quote">Rosalind is a decisive and fair leader who exemplifies strength, wisdom, and empathy. She always possesses a clear vision for the future and is willing to make bold decisions which are grounded in data, expertise, and intuition while remaining open to diverse perspectives.</p>
  <div class="client heading">Marcus Hale</div>
  <div class="client-role">CEO Norvane</div>
</section>

<footer class="site-footer">
  <div class="foot-brand"><span class="dot"></span>TB</div>
  <div class="foot-col" style="left:372px"><h4 class="heading">Quick Link</h4>
    <div class="foot-links"><a href="#">Home</a><a href="#">About us</a><a href="#">services</a><a href="#">Testimonials</a><a href="#">Contct Us</a></div></div>
  <div class="foot-col" style="left:627px"><h4 class="heading">Contact Us</h4>
    <div class="contact-item"><svg width="14" height="14" viewBox="0 0 14 14"><path d="M3 1l2 3-1.5 1.5a8 8 0 0 0 5 5L10 9l3 2-1 2C6 13 1 8 1 2z" fill="#0094D4"/></svg><div><b>Phone</b><span>( 0456 ) 210-3378</span></div></div>
    <div class="contact-item"><svg width="14" height="12" viewBox="0 0 14 12"><rect x="0" y="1" width="14" height="10" rx="1" fill="#0094D4"/><path d="M0 2l7 5 7-5" fill="none" stroke="#232327"/></svg><div><b>Email</b><span>hello@tbranwell.com</span></div></div>
    <div class="contact-item"><svg width="12" height="16" viewBox="0 0 12 16"><path d="M6 0a6 6 0 0 1 6 6c0 4-6 10-6 10S0 10 0 6a6 6 0 0 1 6-6z" fill="#0094D4"/><circle cx="6" cy="6" r="2" fill="#232327"/></svg><div><b>Location</b><span>418 Harbor Lane Portland<br>OR, 97204 United States</span></div></div>
  </div>
  <div class="foot-col" style="left:911px"><h4 class="heading">Follow Us</h4>
    <div class="socials" aria-label="Social media links"><span></span><span></span><span></span><span></span></div></div>
  <div class="foot-rule"></div>
  <div class="copyright">2025 TB, All right Reserved</div>
  <div class="to-top"><svg width="14" height="9" viewBox="0 0 14 9"><path d="M1 8l6-6 6 6" fill="none" stroke="#fff" stroke-width="1.8"/></svg></div>
</footer>

</body>
</html>
```